Photographic Tutorial website

We are looking for a fresh design for a photographic tutorial / workshop website. The website will have the included functions:

* Home (needs to have a login section)
* About Us
* Info about each course / workshop.
* Subscribe to courses and pay online.
* Members Area
* Photo gallery
* Contact us

The website will be implemented with our own made cms. We do not need it to be coded. We have a team ready to do this for us. We only need the PSD layout.

We have attached a mockup design that the client and I have come up with and we need the design to be taken to the next level.

Client also likes:
http://www.vellowindstudio.example/

Photographic Interests

Online

Requirements
Must have
• Must Stand out i.e black backgrounds
Should not have
• Alter the logo in anyway.

```html
<!DOCTYPE html>
<html lang="en">
<head>
<meta charset="utf-8">
<title>Lens Companion – Photographic Tuition</title>
<link href="https://fonts.googleapis.com/css2?family=Roboto:wght@400;500;700&display=swap" rel="stylesheet">
<style>
  :root {
    --bg: #2f2f2f;
    --bg-dark: #262626;
    --panel: #ffffff;
    --text: #ffffff;
    --muted: #c9c9c9;
    --dim: #bdbdbd;
    --red: #d10000;
    --green: #3fbf3f;
    --grey-box: #9a9a9a;
    --moon: #b4b4b4;
    --head-font: "Roboto", Arial, sans-serif;
    --body-font: Arial, Helvetica, sans-serif;
  }
  * { box-sizing: border-box; margin: 0; padding: 0; }
  html, body { width: 1063px; height: 1200px; overflow: hidden; }
  body {
    position: relative;
    background: radial-gradient(ellipse at 50% 30%, #3a3a3a 0%, var(--bg) 50%, var(--bg-dark) 100%);
    color: var(--text);
    font-family: var(--body-font);
  }
  .abs { position: absolute; }

  /* Header */
  .brand { left: 134px; top: 22px; display: flex; align-items: center; gap: 9px; }
  .brand-dot { width: 26px; height: 26px; border-radius: 50%; background: #c62828; }
  .brand-name { font-family: var(--head-font); font-weight: 700; font-size: 28px; color: #ffffff; }
  .nav { right: 132px; top: 36px; display: flex; gap: 25px; font-size: 12.5px; }
  .nav a { color: var(--text); text-decoration: none; }
  .header-rule { left: 0; right: 0; top: 76px; height: 1px; background: #3c3c3c; }

  /* Slider */
  .slider { left: 133px; top: 120px; width: 797px; height: 352px; background: var(--panel); }
  .slide { left: 16px; top: 15px; width: 765px; height: 300px;
    background: linear-gradient(180deg, #6d72c4 0%, #9a8fc8 45%, #5c4a5a 72%, #1d2540 82%, #203060 100%); }
  .dots { left: 648px; top: 327px; display: flex; gap: 6px; }
  .dots span { width: 11px; height: 11px; border-radius: 50%; border: 1.5px solid #555; }
  .dots span.on { background: #555; }
  .arrows { left: 733px; top: 320px; width: 49px; height: 24px; display: flex;
    border: 1px solid #bbb; background: linear-gradient(#f4f4f4, #d8d8d8); }
  .arrows span { flex: 1; display: flex; align-items: center; justify-content: center; }
  .arrows span + span { border-left: 1px solid #aaa; }

  /* Featured cards */
  .card { top: 508px; width: 182px; height: 165px; background: var(--panel); color: #333; }
  .card .pic { position: absolute; left: 6px; top: 9px; width: 168px; height: 120px; }
  .card .cap { position: absolute; left: 6px; top: 137px; font-size: 12px; line-height: 14px; }
  .card .cap a { color: var(--red); text-decoration: none; }
  .pic-autumn { background: linear-gradient(135deg, #c98a1e, #6f7a2a 55%, #3f4f22); }
  .pic-city { background: linear-gradient(180deg, #4f6a9a 0%, #8a8f9a 40%, #6b5a4a 100%); }
  .pic-skyline { background: linear-gradient(180deg, #2a5fb8 0%, #8fb2e0 55%, #2a3a4a 100%); }

  /* Section headings */
  .section-title { font-family: var(--head-font); font-weight: 400; font-size: 15.5px; line-height: 19px; top: 709px; }

  /* Shooting times table */
  .times { left: 133px; top: 761px; width: 245px; border-collapse: collapse; font-size: 14px; }
  .times th { background: #000; color: #fff; font-weight: 400; text-align: left; height: 29px;
    padding-left: 9px; font-family: var(--head-font); font-size: 15px; }
  .times td { height: 29px; color: #eee; padding-left: 9px; font-family: var(--head-font); }
  .times td.c, .times th.c { text-align: center; padding-left: 0; }
  .times th + th, .times td + td { border-left: 2px solid #2f2f2f; }
  .times tr.odd td { background: #8d8d8d; }
  .times tr.even td { background: #7b7b7b; }
  .times tr + tr td { border-top: 1px solid #6a6a6a; }

  /* Moon chart */
  .moon { left: 409px; top: 744px; width: 246px; height: 133px; background: var(--grey-box); }
  .moon-head { height: 34px; background: linear-gradient(#f2f2f2, #cfcfcf); color: #333;
    display: flex; align-items: center; justify-content: space-between; padding: 0 8px;
    font-family: var(--head-font); font-size: 15px; }
  .moon-body { position: relative; padding: 11px 0 0 19px; font-family: var(--head-font);
    font-size: 17px; line-height: 24px; color: #fff; }
  .moon-disc { position: absolute; right: 20px; top: 20px; width: 52px; height: 52px;
    border-radius: 50%; background: var(--moon); }

  /* Check lists */
  .checklist { left: 686px; top: 744px; width: 245px; list-style: none; }
  .checklist li { height: 32px; margin-bottom: 1px; background: var(--grey-box);
    border-top: 1px solid #b5b5b5; font-family: var(--head-font); font-size: 15.5px;
    line-height: 31px; padding-left: 13px; }

  /* Lower row bars */
  .bar { top: 912px; width: 245px; height: 33px; padding-left: 15px; font-weight: 400;
    background: linear-gradient(90deg, #5e5e5e 0%, #3d3d3d 70%, #2a2a2a 100%);
    border-top: 1px solid #777; font-family: var(--head-font); font-size: 15.5px; line-height: 33px; }

  .gallery { left: 133px; top: 969px; width: 245px; display: grid;
    grid-template-columns: repeat(4, 56px); gap: 14px 7px; }
  .gallery div { height: 56px; border: 1px solid #888; }
  .g1 { background: linear-gradient(#8fa8c8, #8d8d8d); }
  .g2 { background: linear-gradient(#b9a6d4, #5a4a6a); }
  .g3 { background: linear-gradient(#1a2030, #b08a3a); }
  .g4 { background: linear-gradient(#9ec2e6, #b0a090); }
  .g5 { background: linear-gradient(#4a78b8, #8a6a3a); }
  .g6 { background: linear-gradient(#2a5fb8, #c8d8ee); }
  .g7 { background: linear-gradient(#6a7a9a, #6a5a4a); }
  .g8 { background: linear-gradient(#2a5fb8, #a0b8d8); }

  .testimonial { left: 409px; top: 966px; width: 247px; height: 130px; font-size: 11.5px; line-height: 14px; color: #fff; }
  .testimonial .quote { float: left; font-family: Georgia, serif; font-size: 44px; line-height: 34px;
    font-weight: 700; margin: 0 6px 0 0; height: 24px; }
  .testimonial .author { position: absolute; right: 0; top: 104px; color: var(--green);
    font-family: var(--head-font); font-size: 15px; font-style: normal; }

  .blog { left: 686px; top: 964px; width: 245px; list-style: none; }
  .blog li { height: 25px; line-height: 22px; font-size: 11.5px; color: var(--dim);
    border-bottom: 1px solid #555; white-space: nowrap; }

  /* Footer */
  .footer-rule { left: 0; right: 0; top: 1124px; height: 1px; background: #3d3d3d; }
  .copyright { left: 132px; top: 1150px; font-size: 12px; color: var(--muted); }
  .partners { right: 132px; top: 1143px; display: flex; gap: 22px; align-items: center;
    font-family: var(--head-font); font-weight: 700; font-size: 19px; color: #ffffff; }
</style>
</head>
<body>

<header>
  <div class="abs brand">
    <span class="brand-dot"></span>
    <span class="brand-name">Lens Companion</span>
  </div>
  <nav class="abs nav">
    <a href="#">Home</a>
    <a href="#">About Us</a>
    <a href="#">Our Courses</a>
    <a href="#">Member's Area</a>
    <a href="#">Contact Us</a>
  </nav>
  <div class="abs header-rule"></div>
</header>

<section class="abs slider">
  <div class="abs slide" role="img" aria-label="City skyline at dusk reflected in a river"></div>
  <div class="abs dots"><span></span><span class="on"></span><span></span><span></span></div>
  <div class="abs arrows">
    <span><svg width="9" height="10"><polygon points="8,0 8,10 0,5" fill="#222"/></svg></span>
    <span><svg width="9" height="10"><polygon points="1,0 1,10 9,5" fill="#222"/></svg></span>
  </div>
</section>

<section>
  <article class="abs card" style="left:133px">
    <div class="pic pic-autumn" role="img" aria-label="Cabin among autumn trees"></div>
    <p class="cap">Praesent nec sapien.<br>by <a href="#">Demo</a></p>
  </article>
  <article class="abs card" style="left:339px">
    <div class="pic pic-city" role="img" aria-label="Old town square seen from above"></div>
    <p class="cap">Praesent nec sapien.<br>by <a href="#">Demo</a></p>
  </article>
  <article class="abs card" style="left:544px">
    <div class="pic pic-autumn" role="img" aria-label="Cabin among autumn trees"></div>
    <p class="cap">Praesent nec sapien.<br>by <a href="#">Demo</a></p>
  </article>
  <article class="abs card" style="left:748px">
    <div class="pic pic-skyline" role="img" aria-label="Waterfront skyline with a tower under blue sky"></div>
    <p class="cap">Praesent nec sapien.<br>by <a href="#">Demo</a></p>
  </article>
</section>

<section>
  <h2 class="abs section-title" style="left:132px">Daily Shooting Times<br>Nautical twilight</h2>
  <table class="abs times">
    <tr><th style="width:109px">Date</th><th class="c" style="width:71px">Start</th><th class="c">End</th></tr>
    <tr class="odd"><td>18 July, 2012</td><td class="c">5:56</td><td class="c">5:56</td></tr>
    <tr class="even"><td>19 July, 2012</td><td class="c">5:56</td><td class="c">5:56</td></tr>
    <tr class="odd"><td>20 July, 2012</td><td class="c">5:56</td><td class="c">5:56</td></tr>
  </table>

  <h2 class="abs section-title" style="left:409px">Moon Phase Chart</h2>
  <div class="abs moon">
    <div class="moon-head">
      <svg width="12" height="14"><polyline points="10,1 3,7 10,13" fill="none" stroke="#222" stroke-width="2.5"/></svg>
      <span>July 2012</span>
      <svg width="12" height="14"><polyline points="2,1 9,7 2,13" fill="none" stroke="#222" stroke-width="2.5"/></svg>
    </div>
    <div class="moon-body">
      Wed, 18<br>Third Quarter<br>06:26 - 16:37
      <div class="moon-disc" role="img" aria-label="Photo of the moon in its third quarter phase"></div>
    </div>
  </div>

  <h2 class="abs section-title" style="left:686px">Photographers Check Lists</h2>
  <ol class="abs checklist">
    <li>1.&nbsp; Wedding Shoot</li>
    <li>2.&nbsp; Pre Shoot</li>
    <li>3.&nbsp; Standard</li>
    <li>4.&nbsp; Lorem Ipsum</li>
  </ol>
</section>

<section>
  <h3 class="abs bar" style="left:133px">Members Gallery</h3>
  <div class="abs gallery" role="img" aria-label="Members' photos of city landmarks">
    <div class="g1"></div><div class="g2"></div><div class="g3"></div><div class="g4"></div>
    <div class="g5"></div><div class="g6"></div><div class="g7"></div><div class="g8"></div>
  </div>

  <h3 class="abs bar" style="left:409px">Testimonials</h3>
  <blockquote class="abs testimonial">
    <span class="quote">&ldquo;</span>Lorem ipsum dolor sit amet, consectetur adipiscing elit. Sed imperdiet, elit nec ndit dictum, justo erat consequat leo, non facilisis augue leo at enim. Nam tristique, nibh vel rhoncus vulputate, risus augue consequat dui, at tincidunt odio ipsum eu urna.
    <cite class="author">Dan Whitfield</cite>
  </blockquote>

  <h3 class="abs bar" style="left:686px">Blog</h3>
  <ul class="abs blog">
    <li>US Guide to 21 Great Photo Locations</li>
    <li>The Wildlife of the US – A New Guide</li>
    <li>Lorem ipsum dolor sit amet, consectetur</li>
    <li>Lorem ipsum dolor sit amet, consectetur elit.</li>
    <li>Lorem ipsum dolor sit amet, consectetur elit.</li>
  </ul>
</section>

<footer>
  <div class="abs footer-rule"></div>
  <p class="abs copyright">Copyright © 2012 Lens Companion</p>
  <div class="abs partners">
    <span>Norvik</span>
    <span>Calder</span>
    <span>Sentrix</span>
  </div>
</footer>

</body>
</html>
```